Tarn Business Card Design Project

We have an existing business card. We are looking to creat a new card for the store. I have attached a my own business so you have a refference of what the current card looks like.

Phone: 1300 571 342
email: kelwood@tarnglazing.com.au
website: www.tarnglazing.com.au
Address: (Inside Kelwood Flooring Yard) 214 Farrow Rd, Ashby Vale VIC 3481
Updates

This is a new business card for our store.

Industry/Entity Type

Business

Requirements
Must have
• Must look similar to the existing card

```html
<!DOCTYPE html>
<html lang="en">
<head>
<meta charset="utf-8">
<title>Tarn Shutters &amp; Blinds – Business Card</title>
<link rel="stylesheet" href="https://fonts.googleapis.com/css2?family=Open+Sans:wght@400;600;700&display=swap">
<style>
  :root {
    --backdrop: #e6e4e1;
    --card: #ffffff;
    --ink: #1c1c1c;
    --grey: #6d6d70;
    --band: #75757a;
    --muted: #8a8a8a;
    --white: #ffffff;
  }
  * { margin: 0; padding: 0; box-sizing: border-box; }
  html, body {
    width: 1200px; height: 900px; overflow: hidden;
    background: var(--backdrop);
    font-family: "Open Sans", Arial, sans-serif;
  }
  .sheet {
    width: 1200px; height: 900px;
    display: flex; align-items: center; justify-content: center; gap: 40px;
  }
  .card {
    position: relative;
    width: 540px; height: 328px;
    background: var(--card);
    box-shadow: 0 6px 18px rgba(0,0,0,0.18);
    overflow: hidden;
  }
  .brand-name {
    font-weight: 400;
    color: var(--ink);
    line-height: 1;
    letter-spacing: -1px;
  }
  .brand-tagline {
    font-weight: 700;
    color: var(--grey);
  }

  /* Front */
  .card-front .top-bar {
    position: absolute; left: 0; top: 0;
    width: 232px; height: 10px; background: var(--ink);
  }
  .card-front .brand { position: absolute; left: 28px; top: 58px; }
  .card-front .brand-name { font-size: 100px; }
  .card-front .brand-tagline { font-size: 22px; margin-top: 2px; margin-left: 4px; }
  .card-front .person { position: absolute; left: 32px; top: 238px; }
  .person-name { font-size: 17px; font-weight: 700; color: var(--ink); }
  .person-role { font-size: 13px; color: var(--muted); margin-top: 1px; }
  .contact {
    position: absolute; right: 24px; top: 62px;
    text-align: right; font-size: 12px; color: var(--ink);
    line-height: 1; list-style: none;
  }
  .contact li { display: flex; justify-content: flex-end; align-items: center; gap: 6px; margin-bottom: 14px; }
  .contact svg { width: 12px; height: 12px; fill: none; stroke: var(--ink); stroke-width: 1.5; }
  .web-band {
    position: absolute; right: 0; top: 150px;
    width: 212px; height: 30px; background: var(--band);
    color: var(--white); font-size: 14px; letter-spacing: 1.5px;
    display: flex; align-items: center; justify-content: center;
  }

  /* Back */
  .card-back { display: flex; flex-direction: column; align-items: center; justify-content: center; }
  .card-back .brand-name { font-size: 118px; }
  .card-back .brand-tagline { font-size: 26px; margin-top: 2px; }
  .card-back .web { font-size: 19px; color: var(--ink); letter-spacing: 1px; margin-top: 30px; }
</style>
</head>
<body>
<main class="sheet">
  <section class="card card-front" aria-label="Business card front">
    <div class="top-bar"></div>
    <div class="brand">
      <div class="brand-name">tarn</div>
      <div class="brand-tagline">Shutters &amp; Blinds</div>
    </div>
    <div class="person">
      <div class="person-name">Daniel Roe</div>
      <div class="person-role">Director</div>
    </div>
    <ul class="contact">
      <li>
        <svg viewBox="0 0 12 12" aria-hidden="true"><circle cx="6" cy="6" r="5"/><path d="M4 3.5c0 2.5 2 4.5 4.5 4.5"/></svg>
        1300 571 342
      </li>
      <li>
        <svg viewBox="0 0 12 12" aria-hidden="true"><rect x="1" y="3" width="10" height="7"/><path d="M1 3l5 4 5-4"/></svg>
        kelwood@tarnglazing.com.au
      </li>
      <li>214 Farrow Rd, Ashby Vale VIC 3481</li>
    </ul>
    <div class="web-band">www.tarnglazing.com.au</div>
  </section>

  <section class="card card-back" aria-label="Business card back">
    <div class="brand-name">tarn</div>
    <div class="brand-tagline">Shutters &amp; Blinds</div>
    <div class="web">www.tarnglazing.com.au</div>
  </section>
</main>
</body>
</html>
```